Brightfern World Learning is to provide global summer programs in the United States through which students from the US and China share experiences, intensive learning, and each other’s cultures. The program seeks to more fully prepare both the US and Chinese students for their college education and future careers in this interdependent world. Chinese students are individually paired with US Students where they will reside US students' home for the period of the program.

Current website: Brightfern World Learning

Need to support both English and Chinese with different font.

Project Deadline Extended
Reason: Because of Thanksgiving Holidays.

Dear Designers,

In order to generate the best design, I uploaded some photos from our global summer program. Please check:

http://brightfernworldlearning.org/photos/

Colette

My company Logo just added to the project.

Sorry for the late update.

Project Deadline Extended
Reason: Due to Thanksgiving holiday, I don't have enough time to provide feedback to all the designers. Colette

Project Deadline Extended
Reason: Holiday season. Need more time for designer and myself.

Target Market(s)

Grade K to 12 students and their parents to sign up the global summer program. Majority audience are from China.

Industry/Entity Type

College

Font styles to use
Sans Serif

Colors
3277b5

Requirements
Must have
• You may check my current website for the summer program content
www.brightfernworldlearning.org
Check these two clips to see what service we provided.
http://www.vidhaven.example/watch?v=7kR3nq41xTm&feature=vh.be
https://www.vidhaven.example/watch?v=W8d2JP6h4oZ

Company Logo are included in the attachment.

Some photos from summer program: http://brightfernworldlearning.org/photos/
The website should show the students one to one relationship.
The website should show homestay part.

I want Photo Slider on each page to share the fun activities.

Each program will be provide a video clip as a summery.

The website should support font of both English and Chinese. I like to see both Chinese and English on the same page instead of switch back and forth. I can add Chinese part later if you leave the room.

Nice to have
• I have a lot of paired pictures. I am wondering if I can use collage of photos as the background.

The design should be playful and fun!

```html
<!DOCTYPE html>
<html lang="en">
<head>
<meta charset="utf-8">
<title>Brightfern World Learning</title>
<link href="https://fonts.googleapis.com/css2?family=Open+Sans:wght@400;600;700&family=Roboto:wght@400;500&display=swap" rel="stylesheet">
<style>
:root{
  --blue:#3277b5;
  --blue-deep:#1a63b0;
  --navy:#0c2f5c;
  --orange:#f0921e;
  --orange-dark:#c9730f;
  --ink:#3d3d3d;
  --grey-band:#5d5f66;
  --white:#ffffff;
  --collage-a:#b9c7e6;
  --collage-b:#d6e0f2;
}
*{box-sizing:border-box;margin:0;padding:0}
html,body{width:1200px;height:2459px;overflow:hidden}
body{font-family:"Open Sans",Arial,sans-serif;color:var(--ink);position:relative;background:var(--collage-b)}
.collage-bg{position:absolute;inset:0;background:linear-gradient(135deg,var(--collage-a),var(--collage-b) 40%,var(--collage-a) 70%,var(--collage-b))}
.page{position:absolute;left:115px;top:0;width:962px;height:2459px;background:var(--white)}
.abs{position:absolute}
h2,h3,.nav a,.footer h4{font-family:"Roboto",Arial,sans-serif;font-weight:400}

/* header */
.brand{left:35px;top:36px;display:flex;align-items:center;gap:10px}
.brand-mark{width:46px;height:46px;border-radius:50%;background:var(--blue)}
.brand-name{font-size:30px;font-weight:700;color:var(--blue)}
.social{display:flex;gap:5px}
.social span{width:17px;height:17px;background:var(--blue);border-radius:2px;display:block}
.social.top{right:32px;top:17px}
.phone{right:32px;top:45px;font-size:15px;font-weight:700;color:var(--blue-deep);display:flex;align-items:center;gap:5px}
.search{right:32px;top:82px;width:268px;height:27px;border:1px solid #c9c9c9;border-radius:3px;font-size:11px;color:#777;padding:5px 10px;background:#fff}
.search svg{position:absolute;right:6px;top:5px}

/* nav */
.nav{left:0;top:136px;width:962px;height:54px;background:var(--orange);border-top:4px solid var(--blue);display:flex;padding-left:84px}
.nav a{color:#fff;font-size:15px;text-decoration:none;padding:0 15px;line-height:50px;white-space:nowrap}
.nav a.active{background:var(--blue)}

/* hero */
.hero{left:0;top:190px;width:962px;height:362px;background:linear-gradient(160deg,#8a7a5e,#c9b58a 45%,#3c3e3f 80%)}
.hero-line{background:rgba(201,140,40,.72);color:#111;font-family:"Roboto",sans-serif;font-size:22px;line-height:32px;padding:0 14px;white-space:nowrap}
.dots{left:469px;top:540px;display:flex;gap:5px}
.dots i{width:5px;height:5px;border-radius:50%;background:#fff;display:block}

/* mission */
.mission-title{left:16px;top:600px;font-size:19px;color:var(--blue)}
.mission-text{left:14px;top:631px;width:510px;font-size:11px;line-height:16.5px}
.read-more{display:inline-block;background:var(--blue);color:#fff;font-size:11px;padding:5px 22px 5px 10px;white-space:nowrap;clip-path:polygon(0 0,100% 0,86% 100%,0 100%)}
.read-more.orange{background:var(--orange)}
.mission-photo{left:580px;top:588px;width:368px;height:200px;background:linear-gradient(120deg,#a9b2bf,#c98078 50%,#8e9fb6)}

/* programs */
.section-rule{left:0;top:836px;width:962px;height:12px;border-top:5px solid var(--blue)}
.section-title{left:425px;top:831px;background:#fff;padding:0 4px;font-size:19px;color:var(--blue)}
.program-photo{width:432px;height:216px}
.program-box{width:503px;height:216px;background:var(--blue);color:#fff}
.ribbon{left:20px;top:-4px}
.ribbon-label{position:absolute;left:30px;top:14px;width:80px;font-family:"Roboto",sans-serif;font-size:15px;line-height:20px;color:#fff}
.program-text{left:180px;top:24px;width:300px;font-size:11px;line-height:16.5px}

/* features */
.feature h3{font-size:19px;color:var(--blue);margin-bottom:12px;white-space:nowrap}
.feature-photo{width:150px;height:86px}
.feature-text{width:230px;font-size:11px;line-height:16px}

/* gallery */
.gallery{left:0;top:1877px;width:962px;height:249px;background:var(--grey-band)}
.gallery-tab{left:424px;top:1866px;width:130px;height:54px;background:var(--orange);color:#fff;font-family:"Roboto",sans-serif;font-size:20px;text-align:center;line-height:52px;box-shadow:0 4px 0 var(--orange-dark)}
.gallery-photo{top:1938px;height:148px}
.arrow{width:50px;height:50px;border-radius:50%;background:rgba(0,0,0,.35);top:1987px}

/* footer */
.footer{left:0;top:2126px;width:962px;height:300px;background:var(--blue-deep);color:#fff}
.footer h4{font-size:18px;margin-bottom:18px;white-space:nowrap}
.footer .col{position:absolute;top:38px}
.footer .info{font-size:11px;line-height:20px}
.footer .nav-list{font-family:"Roboto",sans-serif;font-size:15px;line-height:23px;white-space:nowrap}
.nav-list .current{color:var(--orange)}
.field{background:#fff;color:#333;font-size:9px;padding:5px 7px;margin-bottom:6px;width:190px}
.join{display:flex;width:190px;height:30px}
.join .email{background:#fff;color:#333;font-size:9px;flex:1;padding:9px 8px}
.join .btn{background:var(--orange);font-size:11px;padding:8px 14px 0 14px;clip-path:polygon(0 0,100% 0,82% 100%,0 100%);width:50px}
.submit{display:inline-block;background:var(--orange);font-size:12px;padding:7px 40px 7px 26px;clip-path:polygon(0 0,100% 0,86% 100%,0 100%)}
.bottom-bar{left:0;top:2426px;width:962px;height:33px;background:var(--navy);color:#fff;font-size:11px;padding:9px 32px}
.social.bottom{right:32px;top:8px}
</style>
</head>
<body>
<div class="collage-bg" role="img" aria-label="Collage of paired student photos tinted light blue"></div>

<div class="page">
  <div class="abs brand"><span class="brand-mark"></span><span class="brand-name">Brightfern</span></div>
  <div class="abs social top"><span></span><span></span><span></span><span></span></div>
  <div class="abs phone">
    <svg width="12" height="14" viewBox="0 0 12 14"><path d="M3 1 L5 4 L3.5 5.5 Q5 9 8 10.5 L9.5 9 L12 11 L10 13.5 Q2 12 0.5 3 Z" fill="#f0b400"/></svg>
    1-800-555-0142
  </div>
  <div class="abs search">Search
    <svg width="14" height="14" viewBox="0 0 14 14"><circle cx="6" cy="6" r="4" fill="none" stroke="#888" stroke-width="1.5"/><path d="M9 9 L13 13" stroke="#888" stroke-width="1.5"/></svg>
  </div>

  <nav class="abs nav">
    <a class="active">Home</a><a>Harlow Summer Program</a><a>Lakeview Summer Camp</a><a>Whole Year Program</a><a>Wendmoor University</a>
  </nav>

  <div class="abs hero" role="img" aria-label="Students working together around a classroom table"></div>
  <p class="abs hero-line" style="left:286px;top:337px">Lorem ipsum dolor sit amet</p>
  <p class="abs hero-line" style="left:262px;top:379px">consectetur adipisicing elit sed do</p>
  <div class="abs dots"><i></i><i></i><i></i></div>

  <h2 class="abs mission-title">Our Mission</h2>
  <p class="abs mission-text">Brightfern World Learning is to help American students and Chinese students to break the barriers between the two different cultures, experiences and education backgrounds by providing a global summer program in the U.S. with American students and Chinese students one to one paired, home stay in US families, intensive learning and culture adventure activities, and get them fully prepared for their college education and career developments in this interdependent world.</p>
  <span class="abs read-more" style="left:14px;top:752px">Read more</span>
  <div class="abs mission-photo" role="img" aria-label="Two paired students wrapped in Chinese and American flags"></div>

  <div class="abs section-rule"></div>
  <h2 class="abs section-title">Our Program</h2>

  <div class="abs program-photo" style="left:15px;top:874px;background:linear-gradient(100deg,#6d4d3c,#c79a7a 50%,#8c6250)" role="img" aria-label="Students presenting on a stage"></div>
  <div class="abs program-box" style="left:447px;top:893px">
    <svg class="abs ribbon" width="130" height="124" viewBox="0 0 130 124"><polygon points="0,4 10,0 10,4" fill="#c9730f"/><polygon points="10,0 120,0 120,124 65,100 10,124" fill="#f0921e"/><polygon points="120,0 130,8 120,8" fill="#c9730f"/></svg>
    <div class="ribbon-label">Harlow Summer Program</div>
    <p class="abs program-text">Monday to Friday: half-time courses on innovation and entrepreneurship Harlow high school students with the United States, half of the time for the community to explore internship or downtown Chicago. The group game demos, invited Searchly, Dealhive, Evenlight and other well-known companies doing innovative expert judgment before the end.</p>
    <span class="abs read-more orange" style="left:180px;top:168px">Read more</span>
  </div>

  <div class="abs program-photo" style="left:15px;top:1139px;background:linear-gradient(100deg,#8a5a4c,#d9c0a8 50%,#8d5f55)" role="img" aria-label="Group photo of camp students"></div>
  <div class="abs program-box" style="left:447px;top:1153px">
    <svg class="abs ribbon" width="130" height="124" viewBox="0 0 130 124"><polygon points="0,4 10,0 10,4" fill="#c9730f"/><polygon points="10,0 120,0 120,124 65,100 10,124" fill="#f0921e"/><polygon points="120,0 130,8 120,8" fill="#c9730f"/></svg>
    <div class="ribbon-label">Lakeview Summer Camp</div>
    <p class="abs program-text">Ed prior to registration. One week prior to the start of camp we will have trainings to prepare you on how to be a great teen leader. This program will include helping and shadowing the counselors in Sports and some specialty camps.</p>
    <span class="abs read-more orange" style="left:180px;top:122px">Read more</span>
  </div>

  <div class="abs program-photo" style="left:15px;top:1401px;background:linear-gradient(100deg,#6f7f86,#c7b7a0 55%,#7d8a94)" role="img" aria-label="Two paired students in front of a city skyline"></div>
  <div class="abs program-box" style="left:447px;top:1415px">
    <svg class="abs ribbon" width="130" height="124" viewBox="0 0 130 124"><polygon points="0,4 10,0 10,4" fill="#c9730f"/><polygon points="10,0 120,0 120,124 65,100 10,124" fill="#f0921e"/><polygon points="120,0 130,8 120,8" fill="#c9730f"/></svg>
    <div class="ribbon-label">Whole Year Program</div>
    <p class="abs program-text">We partner with schools, one in America and one in China, so that the students can do projects together; learning, living and having fun together under teachers' guidance.</p>
    <span class="abs read-more orange" style="left:180px;top:125px">Read more</span>
  </div>

  <div class="abs feature" style="left:30px;top:1672px">
    <h3>One to one relationship</h3>
    <div class="abs feature-photo" style="left:0;top:40px;background:linear-gradient(120deg,#7d8fa5,#c8b0a0)" role="img" aria-label="Paired students in the city"></div>
    <p class="abs feature-text" style="left:167px;top:38px">Lorem ipsum dolor sit amet, consectetur adipisicing elit, sed do eiusmod tempor incididunt ut</p>
    <span class="abs read-more" style="left:167px;top:104px">Read more</span>
  </div>
  <div class="abs feature" style="left:546px;top:1672px">
    <h3>Home stay</h3>
    <div class="abs feature-photo" style="left:0;top:40px;background:linear-gradient(120deg,#a57a5c,#d8b39a)" role="img" aria-label="Students sharing a meal at a host family table"></div>
    <p class="abs feature-text" style="left:167px;top:38px">Lorem ipsum dolor sit amet, consectetur adipisicing elit, sed do eiusmod tempor incididunt ut</p>
    <span class="abs read-more" style="left:167px;top:104px">Read more</span>
  </div>

  <div class="abs gallery" role="img" aria-label="Dimmed collage of activity photos"></div>
  <div class="abs gallery-tab">Gallery</div>
  <div class="abs gallery-photo" style="left:34px;width:215px;background:linear-gradient(180deg,#c9d3dc,#5f8a52)" role="img" aria-label="Students biking in a park"></div>
  <div class="abs gallery-photo" style="left:259px;width:216px;background:linear-gradient(120deg,#b9b0a0,#6c6a66)" role="img" aria-label="Students playing in a courtyard"></div>
  <div class="abs gallery-photo" style="left:485px;width:216px;background:linear-gradient(180deg,#7fb0df,#3e86a8 60%,#2e6b3e)" role="img" aria-label="Students at the lakefront skyline"></div>
  <div class="abs gallery-photo" style="left:711px;width:217px;background:linear-gradient(120deg,#8c8a7a,#c7a68c)" role="img" aria-label="Group of students outdoors"></div>
  <div class="abs arrow" style="left:15px"><svg width="50" height="50" viewBox="0 0 50 50"><polygon points="30,15 30,35 17,25" fill="#fff"/></svg></div>
  <div class="abs arrow" style="left:897px"><svg width="50" height="50" viewBox="0 0 50 50"><polygon points="20,15 20,35 33,25" fill="#fff"/></svg></div>

  <footer class="abs footer">
    <div class="col" style="left:33px">
      <h4>About Us</h4>
      <div class="info">
        <p style="font-weight:700"><svg width="12" height="9" viewBox="0 0 12 9" style="margin-right:6px"><rect width="12" height="9" fill="#cfe0f5"/><path d="M0 0 L6 5 L12 0" stroke="#1a63b0" fill="none"/></svg>hello@brightfern.example</p>
        <p style="margin-top:20px;padding-left:18px">P: +1 555 222-0101<br>F: +1 555 222-0101</p>
        <p style="margin-top:20px;padding-left:18px;position:relative"><svg width="10" height="13" viewBox="0 0 10 13" style="position:absolute;left:0;top:4px"><path d="M5 13 L1 6 A4 4 0 1 1 9 6 Z" fill="#cfe0f5"/></svg>48 Alder Lane, Suite 12<br>United States, GA 30000</p>
      </div>
    </div>
    <div class="col" style="left:259px">
      <h4>Navigation</h4>
      <div class="nav-list"><p class="current">Home</p><p>Harlow Summer Program</p><p>Lakeview Summer Camp</p><p>Whole Year Program</p><p>Wendmoor University</p></div>
    </div>
    <div class="col" style="left:477px">
      <h4>Newsltetter Sign up</h4>
      <p class="info" style="width:205px;line-height:18px">Lorem ipsum dolor sit amet, consectetur adipisicing elit, sed do eiusmod tempor incididunt ut labore et dolore magna aliqua. Ut</p>
      <div class="join" style="margin-top:28px"><span class="email">Email address</span><span class="btn">Join</span></div>
      <p class="info" style="margin-top:4px">We respect your privacy</p>
    </div>
    <div class="col" style="left:739px">
      <h4>Feedback</h4>
      <div class="field">Name</div>
      <div class="field">E-mail</div>
      <div class="field" style="height:94px">Message</div>
      <span class="submit">Submit</span>
    </div>
  </footer>
  <div class="abs bottom-bar">© 2013, Copy Right for Brightfern World Learning
    <div class="abs social bottom"><span></span><span></span><span></span><span></span></div>
  </div>
</div>
</body>
</html>
```